Body corporate management needs business principle flyer design

We need a one page A4 flyer design for our business principles.
We manage body corporates and strata properties.
TenuraKeep is a new initiative for our company. Its a label that we have given to our principles of business that drive our people, systems and processes to give assurance to our clients that every detail matters.
We would like to be able to include this design in future brochure so we are after 1 x portrait and 1 x landscape.
The design needs to portray professionalism.
We would like to see designs that use the colour red. (see attached logo).

Target Market(s)

Professionals

Industry/Entity Type

Business

Font styles to use
Sans Serif

Requirements
Must have
• TenuraKeep logo, provide the design file and as pdf
Nice to have
• the use of the colour red from the logo

```html
<!DOCTYPE html>
<html lang="en">
<head>
<meta charset="utf-8">
<title>TenuraKeep Business Principles</title>
<link rel="stylesheet" href="https://fonts.googleapis.com/css2?family=Roboto:wght@400;700&family=Roboto+Condensed:wght@700&display=swap">
<style>
  :root {
    --brand-red: #e43a2f;
    --heading-red: #b3141b;
    --sky: #d5e1e9;
    --tag-blue: #d9e4ec;
    --charcoal: #4b4b4d;
    --ink: #3f3f41;
    --paper: #ffffff;
    --stage: #eeeeee;
  }
  * { box-sizing: border-box; margin: 0; padding: 0; }
  html, body { width: 1200px; height: 1200px; overflow: hidden; }
  body {
    background: var(--stage);
    font-family: "Roboto", Arial, sans-serif;
    color: var(--ink);
  }
  .flyer {
    position: absolute;
    left: 176px;
    top: 20px;
    width: 848px;
    height: 1160px;
    background: linear-gradient(to bottom, var(--sky) 0, var(--sky) 50%, var(--charcoal) 50%, var(--charcoal) 100%);
    box-shadow: 0 6px 24px rgba(0,0,0,0.18);
  }
  .name-box {
    position: absolute;
    left: 40px;
    top: 40px;
    width: 300px;
    height: 120px;
    background: var(--paper);
    display: flex;
    align-items: center;
    padding-left: 26px;
  }
  .company-name {
    font-family: "Roboto", Arial, sans-serif;
    font-weight: 700;
    font-size: 36px;
    color: var(--charcoal);
  }
  .content {
    position: absolute;
    left: 40px;
    top: 160px;
    width: 768px;
    bottom: 40px;
    background: var(--paper);
  }
  .banner {
    background: var(--brand-red);
    color: var(--paper);
    font-family: "Roboto Condensed", Arial, sans-serif;
    font-weight: 700;
    font-size: 22px;
    line-height: 1.25;
    padding: 14px 26px;
  }
  .experience {
    background: var(--charcoal);
    color: #e6e6e6;
    padding: 14px 26px 18px;
    font-size: 13.5px;
    line-height: 1.4;
  }
  .experience h2 {
    font-size: 15px;
    font-weight: 700;
    color: var(--paper);
    margin-bottom: 4px;
  }
  .principles { padding: 16px 26px 0; }
  .principle { margin-bottom: 8px; }
  .principle h3 {
    display: inline-block;
    background: var(--tag-blue);
    color: var(--heading-red);
    font-size: 14.5px;
    font-weight: 700;
    padding: 2px 30px 2px 4px;
    margin-bottom: 3px;
  }
  .principle p {
    font-size: 13.5px;
    line-height: 1.4;
  }
</style>
</head>
<body>
  <main class="flyer">
    <div class="name-box">
      <span class="company-name">TenuraKeep</span>
    </div>
    <section class="content">
      <h1 class="banner">TenuraKeep is our principles of business that drive our people, systems and processes to give assurance to our clients that every detail matters.</h1>
      <div class="experience">
        <h2>Client Experience</h2>
        <p>Our promise is to pursue excellence and to continually deliver a solutions based service. We achieve this through active engagement, open channels of communication and a serviced led team with the dedicated resources to listen, engage and implement.</p>
      </div>
      <div class="principles">
        <article class="principle">
          <h3>Loyalty</h3>
          <p>We seek to develop a life-time relationship with our clients, building trust by acting with integrity, honesty and courtesy. We achieve this due to our expert approach to strata management and providing a responsive service to our clients.</p>
        </article>
        <article class="principle">
          <h3>Education and Guidance</h3>
          <p>We endeavor to always be proactive in client education and guidance. This is achieved by our internal and external communications, comprehensive training programs and cross-departmental collaboration of knowledge sharing.</p>
        </article>
        <article class="principle">
          <h3>Compliance and Governance</h3>
          <p>We engage and own a position of 'every detail matters'. We give due diligence to the relevant state and national legislations with which we, our clients and our stakeholders must comply. We regulate and achieve this through a robust system of internal processes and protocols which structure and confirm our deliverables are in line with regulations.</p>
        </article>
        <article class="principle">
          <h3>Systems and processes</h3>
          <p>We strive to be the best in our field, by implementing efficiencies without compromising service quality, accuracy or compliance. We continually seek to achieve this by reviewing, updating and adopting continuous improvement strategies, systems and quality processes that deliver outcomes.</p>
        </article>
        <article class="principle">
          <h3>Quality and Commitment</h3>
          <p>We invest in the recruitment and retention of a quality and diverse team of experienced professionals with a strong focus on continual professional development. As committed and skilled individuals, we actively promote the cross-departmental collaboration with one another to deliver a well rounded offering.</p>
        </article>
        <article class="principle">
          <h3>Delivery</h3>
          <p>We empower our teams to deliver an outstanding client service and to be accountable for their actions. We will make sure every detail matters, provide valuable insight and supply information in a clear and timely manner.</p>
        </article>
        <article class="principle">
          <h3>Integrity</h3>
          <p>Our approach to strata management is bound by honesty and a strong set of moral principles. We act in our clients' best interests with diligence and transparency for understanding and accountability.</p>
        </article>
        <article class="principle">
          <h3>Continuous Improvement</h3>
          <p>Our goal is to continually evolve to better our offering and to be adaptable and responsive to change. Our infrastructure supports us to continually mould into the business that is right for our clients.</p>
        </article>
        <article class="principle">
          <h3>Ethical Stance</h3>
          <p>We aim to create a community of ethical business relationships where we contribute our values and services to give our clients outstanding reassurance of our abilities.</p>
        </article>
      </div>
    </section>
  </main>
</body>
</html>
```